Business Card Design Project

I want a design for my business cards based on an excisting logo design.

Target Market(s)

Marketeers, PR-peeps, CEO's, decisionmakers, entrepreneurs

Industry/Entity Type

Business

Requirements
Nice to have
• Some visual interest on the back too
Should not have
• Sarif on the font

```html
<!DOCTYPE html>
<html lang="nl">
<head>
<meta charset="utf-8">
<title>LimeLeafPR – visitekaartje</title>
<link rel="stylesheet" href="https://fonts.googleapis.com/css2?family=Dosis:wght@400;500;700&display=swap">
<style>
  :root {
    --lime: #b2cc1e;
    --lime-soft: #c6dc4a;
    --charcoal: #2f2f2f;
    --ink: #4a4a4a;
    --grey-word: #8a8a8a;
    --paper: #ffffff;
    --stage: #dfe5e8;
    --rule: #555555;
  }
  * { margin: 0; padding: 0; box-sizing: border-box; }
  html, body {
    width: 1200px; height: 960px; overflow: hidden;
    background: var(--stage);
    font-family: "Dosis", sans-serif;
  }
  .stage { position: relative; width: 1200px; height: 960px; }
  .card {
    position: absolute; left: 300px; width: 600px; height: 340px;
    overflow: hidden;
    box-shadow: 0 6px 18px rgba(0,0,0,0.18);
  }
  .card--front { top: 110px; background: var(--paper); }
  .card--back { top: 510px; background: var(--charcoal); }

  /* front */
  .brand {
    position: absolute; left: 30px; top: 30px;
    display: flex; align-items: center; gap: 16px;
  }
  .brand__dot {
    width: 64px; height: 64px; border-radius: 50%;
    background: var(--lime);
  }
  .brand__name {
    font-size: 50px; font-weight: 500; color: var(--grey-word);
    letter-spacing: 1px; line-height: 1;
  }
  .tagline {
    position: absolute; left: 112px; top: 98px; right: 0;
    background: var(--lime);
    color: var(--ink);
    font-size: 16px; line-height: 20px; padding: 3px 10px;
    white-space: nowrap;
  }
  .holder {
    position: absolute; left: 30px; right: 30px; top: 170px;
    border-top: 1.5px solid var(--rule);
    border-bottom: 1.5px solid var(--rule);
    padding: 10px 0 8px;
    font-size: 30px; font-weight: 500; color: var(--ink);
    line-height: 1.2;
  }
  .contact {
    position: absolute; top: 240px;
    font-size: 17px; font-style: normal; color: var(--ink); line-height: 1.45;
  }
  .contact--left { left: 30px; }
  .contact--right { left: 370px; }
  .contact__label { color: var(--lime); font-weight: 700; }

  /* back */
  .back__circle {
    position: absolute; width: 420px; height: 420px; border-radius: 50%;
    right: -90px; top: -40px;
    background: var(--lime);
  }
  .back__web {
    position: absolute; left: 60px; top: 155px;
    font-size: 24px; font-weight: 500; color: var(--lime-soft);
    letter-spacing: 1px;
  }
</style>
</head>
<body>
<main class="stage">
  <section class="card card--front" aria-label="Voorzijde visitekaartje">
    <div class="brand">
      <span class="brand__dot"></span>
      <span class="brand__name">LimeLeafPR</span>
    </div>
    <p class="tagline">Heldere en doelgerichte adviezen voor pers, merk en communicatie</p>
    <h1 class="holder">Mara Linden</h1>
    <address class="contact contact--left">
      <div><span class="contact__label">T:</span> +31(0)6 12345678</div>
      <div><span class="contact__label">E:</span> mara.linden@limeleafpr.nl</div>
      <div><span class="contact__label">chirp</span>.example/_limeleafpr</div>
    </address>
    <address class="contact contact--right">
      <div>Bessenlaan 12</div>
      <div>6701 AB Lindeveld</div>
      <div><span class="contact__label">social</span>.example/limeleafpr</div>
    </address>
  </section>

  <section class="card card--back" aria-label="Achterzijde visitekaartje">
    <span class="back__circle"></span>
    <p class="back__web">limeleafpr.nl</p>
  </section>
</main>
</body>
</html>
```